Build a landing page for restaurant reservation

The idea is the following:

1. User enters landing page and selects type of reservation (Business, Romantic, Birthday, Casual, etc.)
2. Then user is presented with a menu, where he will select what he wants served. On this page the user can as well select a certain decoration for the table (flowers, roses, birthday cake, etc)
3. He will then fill out a form with his details (date and contact info for reservation)
4. He will receive an email confirmation, as well as the business will be notified of his entries through email, so they can proceed to make the appropriate arrangement

Attached is a PDF with our idea of design and flow.

NOTE: WE WILL UPGRADE PRIZE IF WE ARE SATISFIED WITH WORK

```html
<!DOCTYPE html>
<html lang="en">
<head>
<meta charset="utf-8">
<title>Valeta — Restaurant Reservation Landing Page</title>
<link rel="stylesheet" href="https://fonts.googleapis.com/css2?family=Cinzel:wght@400;700&family=Open+Sans:ital,wght@0,400;0,600;1,400&display=swap">
<style>
  :root {
    --ink: #0f0f0f;
    --paper: #ffffff;
    --hero-dark: #1c1612;
    --hero-mid: #3b2f26;
    --hero-light: #5a4838;
    --muted: #8b8580;
    --text: #3a3a3a;
    --line: #dcdcdc;
    --accent: #5b4536;
    --quote-rule: #8a7a6c;
    --bread-a: #c99a5c;
    --bread-b: #7a5a38;
  }
  * { box-sizing: border-box; margin: 0; padding: 0; }
  html, body { width: 1200px; height: 610px; overflow: hidden; background: var(--paper); }
  body { position: relative; font-family: "Open Sans", Arial, sans-serif; color: var(--text); }

  .sidebar {
    position: absolute; left: 0; top: 0; width: 375px; height: 610px;
    background: var(--ink); color: var(--paper); padding: 90px 0 0 50px;
  }
  .sidebar__brand {
    font-family: "Cinzel", Georgia, serif; font-weight: 400;
    font-size: 46px; letter-spacing: 5px; line-height: 1;
  }
  .sidebar__features { list-style: none; margin-top: 54px; }
  .sidebar__features li {
    font-family: "Cinzel", Georgia, serif; font-size: 21px; text-transform: uppercase;
    letter-spacing: 1px; line-height: 47px; white-space: nowrap;
  }

  .page { position: absolute; left: 375px; top: 0; width: 825px; height: 610px; }

  .topbar {
    height: 45px; background: var(--paper); display: flex;
    align-items: center; justify-content: space-between; padding: 0 72px 0 118px;
  }
  .topbar__brand { font-family: "Cinzel", Georgia, serif; font-size: 13px; letter-spacing: 2px; color: var(--ink); }
  .topbar__contact { font-size: 8.5px; color: var(--text); }

  .hero {
    position: relative; height: 392px;
    background: radial-gradient(ellipse at 30% 60%, var(--hero-light) 0%, var(--hero-mid) 35%, var(--hero-dark) 80%);
  }
  .hero__intro { position: absolute; left: 118px; top: 36px; width: 260px; color: var(--paper); }
  .hero__title {
    font-family: "Cinzel", Georgia, serif; font-weight: 700; text-transform: uppercase;
    font-size: 21px; line-height: 26px; letter-spacing: 0.3px;
  }
  .hero__lead { margin-top: 8px; font-size: 8.5px; line-height: 13px; color: #d8d2cc; }
  .quote {
    margin-top: 20px; padding-left: 12px; border-left: 1px solid var(--quote-rule);
    font-size: 8.5px; line-height: 13px; color: #d8d2cc; font-style: italic;
  }
  .quote cite { font-style: normal; font-weight: 600; color: var(--paper); letter-spacing: 0.4px; }

  .booking {
    position: absolute; left: 459px; top: 40px; width: 256px; height: 325px;
    background: var(--paper); padding: 10px 22px 0; text-align: center;
  }
  .booking__icon { display: block; margin: 0 auto; }
  .booking__title { font-family: "Cinzel", Georgia, serif; font-size: 21px; color: var(--ink); margin-top: 2px; letter-spacing: 0.5px; }
  .booking__note { font-size: 7.5px; line-height: 11px; color: var(--muted); margin-top: 3px; }
  .booking__field {
    display: flex; align-items: center; justify-content: space-between;
    width: 100%; height: 22px; margin-top: 12px;
    border: 1px solid var(--line); font-size: 7.5px; color: var(--muted);
    text-align: left; padding: 0 7px;
  }
  .booking__field--area { height: 42px; align-items: flex-start; padding-top: 6px; }
  .booking__submit {
    display: inline-block; margin-top: 16px; background: var(--accent); color: var(--paper);
    font-size: 6.5px; font-weight: 600; letter-spacing: 1px; padding: 6px 12px;
  }

  .services { position: absolute; left: 0; top: 437px; width: 825px; height: 173px; background: var(--paper); }
  .services__photo {
    position: absolute; left: 118px; top: 34px; width: 335px; height: 139px;
    background: linear-gradient(135deg, var(--bread-a) 0%, var(--bread-b) 60%, #4a3524 100%);
  }
  .services__body { position: absolute; left: 465px; top: 36px; width: 300px; }
  .services__title { font-family: "Cinzel", Georgia, serif; font-size: 21px; color: var(--ink); letter-spacing: 0.3px; line-height: 26px; }
  .services__lead { font-size: 8px; line-height: 12px; color: var(--muted); margin-top: 3px; }
  .services__list { list-style: none; margin-top: 6px; }
  .services__list li { display: flex; align-items: center; gap: 6px; font-size: 8px; line-height: 19px; color: var(--text); }
</style>
</head>
<body>
  <aside class="sidebar">
    <h1 class="sidebar__brand">VALETA</h1>
    <ul class="sidebar__features">
      <li>Fully Responsive</li>
      <li>3 Colors Ready</li>
      <li>Grid Framework</li>
      <li>Well Documented</li>
      <li>Vector Icons</li>
      <li>Lightweight</li>
    </ul>
  </aside>

  <main class="page">
    <header class="topbar">
      <span class="topbar__brand">VALETA</span>
      <span class="topbar__contact">Open: 12pm–12am | 18 Harbor Lane Oakridge | +1 555 014 2290</span>
    </header>

    <section class="hero" role="img" aria-label="Dark close-up photograph of rustic bread loaves on a wooden table">
      <div class="hero__intro">
        <h2 class="hero__title">Perfect Pub or<br>Cafe Landing Page</h2>
        <p class="hero__lead">Pick the occasion, choose your menu and table decor, then book a date. We confirm by email and prepare everything.</p>
        <p class="quote">“Roses on the table and our menu ready on arrival, a perfect evening.” <cite>ELIAS MORROW</cite></p>
        <p class="quote">“They set a birthday cake and flowers exactly as I asked.” <cite>MARTA QUINN</cite></p>
      </div>

      <form class="booking">
        <svg class="booking__icon" width="14" height="14" viewBox="0 0 14 14" aria-hidden="true">
          <rect x="1" y="2.5" width="12" height="10.5" fill="none" stroke="#777" stroke-width="1.2"/>
          <rect x="1" y="2.5" width="12" height="3" fill="#777"/>
          <line x1="4" y1="0.5" x2="4" y2="3.5" stroke="#777" stroke-width="1.2"/>
          <line x1="10" y1="0.5" x2="10" y2="3.5" stroke="#777" stroke-width="1.2"/>
        </svg>
        <h3 class="booking__title">BOOK A TABLE</h3>
        <p class="booking__note">Choose the occasion, menu and decor, then leave your details for email confirmation.</p>
        <span class="booking__field">Reservation Type: Business, Romantic, Birthday<svg width="7" height="5" viewBox="0 0 7 5" aria-hidden="true"><path d="M0.5 0.5 L3.5 4 L6.5 0.5" fill="none" stroke="#999" stroke-width="1"/></svg></span>
        <span class="booking__field">Menu and Table Decoration<svg width="7" height="5" viewBox="0 0 7 5" aria-hidden="true"><path d="M0.5 0.5 L3.5 4 L6.5 0.5" fill="none" stroke="#999" stroke-width="1"/></svg></span>
        <span class="booking__field">Date and Time</span>
        <span class="booking__field booking__field--area">Your Name, Email and Phone</span>
        <span class="booking__submit">FIND A TABLE</span>
      </form>
    </section>

    <section class="services">
      <div class="services__photo" role="img" aria-label="Photograph of baguettes standing in wicker baskets"></div>
      <div class="services__body">
        <h2 class="services__title">LIST OF SERVICES</h2>
        <p class="services__lead">Every occasion gets its own menu and table decor: flowers, roses or a cake, set before you arrive.</p>
        <ul class="services__list">
          <li><svg width="9" height="9" viewBox="0 0 9 9" aria-hidden="true"><rect width="9" height="9" fill="#555"/><path d="M2 4.6 L3.8 6.3 L7 2.8" fill="none" stroke="#fff" stroke-width="1.2"/></svg>New Year Eve</li>
          <li><svg width="9" height="9" viewBox="0 0 9 9" aria-hidden="true"><rect width="9" height="9" fill="#555"/><path d="M2 4.6 L3.8 6.3 L7 2.8" fill="none" stroke="#fff" stroke-width="1.2"/></svg>Birthday Party</li>
          <li><svg width="9" height="9" viewBox="0 0 9 9" aria-hidden="true"><rect width="9" height="9" fill="#555"/><path d="M2 4.6 L3.8 6.3 L7 2.8" fill="none" stroke="#fff" stroke-width="1.2"/></svg>Wedding</li>
        </ul>
      </div>
    </section>
  </main>
</body>
</html>
```